Craft Portuguese Gin Distillery launching new gin into international market

We are going to launch two new gins:
1. An aged version of the Volka Sereno, one that already exists - aged in port casks. This will be a 500ml bottle. Bottle not defined yet - Check www.sipvolka.example
2. A new gin with a lower ABV (lower strength), to satisfy both connoisseurs and "ordinary"; customers. We want to stay with the branding line. The label must appeal to the customer to try the gin, must stand out on a shelf that is full of other spirits. We want to pass on the idea of a premium gin. No botle selected yet. For this gin we may use only a label or a complete decorated bottle. Take care of the legal demands that have to go onto the label - we can help with this later on.
Notes:
- The distillery's name is Volka - Premium Spirits (logo attached)
- Our first gin is called Volka Sereno (logo attached)
- No names selected for either of these gins;
- We have a moto that we would like to see on the bottle:
"Drink to remember, not to forget!";
- Our gins have a unique botanical that is fig tree bark, we are portuguese and we are very fond of the fig image attached.
- Attached we send some documents where you can learn about the story of the gin and also for you to get to know us little better.
- If you wish to suggest a bottle, please look-up these two web sites:
https://www.brimcraft.example/en
https://www.lumavessel.example/
Please contact us for any further information.
Thank you

Target Market(s)

Spirits worldwide

Colors

Designer to choose colors to be used in the design.

Requirements
Must have
• Mandatory Legal information for spirit drinks
• Place for:
• - Producer / bottler (name and addres)
• - Origin fo the product - Product from Portugal
• - ABV and Capacity
• - Type of product: "Londo Dry Gin"
Nice to have
• - We have a moto that we would like to see on the bottle:
• "quot;Drink to remember, not to forget!";
• - Our gins have a unique botanical that is fig tree bark, we are portuguese and we are very fond of the fig image attached.

```html
<!DOCTYPE html>
<html lang="en">
<head>
<meta charset="utf-8">
<title>Volka Sereno — London Dry Gin Range</title>
<link rel="stylesheet" href="https://fonts.googleapis.com/css2?family=Cormorant+Garamond:wght@500;600&family=Oswald:wght@500&family=Parisienne&display=swap">
<style>
  :root {
    --bg: #ececec;
    --brand-red: #9c2a2b;
    --label-white: #fbfaf6;
    --fig-light: #efe6d2;
    --fig-mid: #ddcfae;
    --fig-deep: #cdbb92;
    --panel-dark: #333335;
    --panel-text: #f4f1ea;
    --ink: #2a2a2a;
    --band-orange: #b8441f;
    --band-red: #b32a2a;
    --band-crimson: #a11d3a;
    --glass-pale: #e8e5b3;
    --glass-dark: #3b1619;
    --glass-rose: #f1d3d2;
    --cap-copper: #b9735f;
    --cap-wine: #7d3b3d;
    --cap-rose: #c27a8c;
  }
  * { margin: 0; padding: 0; box-sizing: border-box; }
  html, body { width: 1200px; height: 848px; overflow: hidden; }
  body {
    background: var(--bg);
    font-family: "Cormorant Garamond", Georgia, serif;
    position: relative;
  }
  .brand-name {
    position: absolute;
    top: 98px;
    left: 0;
    width: 1200px;
    text-align: center;
    color: var(--brand-red);
    font-weight: 600;
    font-size: 58px;
    line-height: 1;
  }
  .bottle {
    position: absolute;
    top: 274px;
    width: 127px;
    height: 497px;
  }
  .bottle--classic { left: 341px; }
  .bottle--aged { left: 538px; }
  .bottle--light { left: 733px; }
  .bottle__glass--pale { fill: var(--glass-pale); }
  .bottle__glass--dark { fill: var(--glass-dark); }
  .bottle__glass--rose { fill: var(--glass-rose); }
  .bottle__cap--copper { fill: var(--cap-copper); }
  .bottle__cap--wine { fill: var(--cap-wine); }
  .bottle__cap--rose { fill: var(--cap-rose); }

  .label-wrap { position: absolute; top: 542px; width: 118px; height: 123px; }
  .label-wrap--classic { left: 349px; }
  .label-wrap--aged { left: 546px; }
  .label-wrap--light { left: 741px; }
  .label {
    position: absolute;
    left: 8px;
    top: 0;
    width: 110px;
    height: 123px;
    background: var(--label-white);
    overflow: hidden;
  }
  .label__fig {
    position: absolute;
    inset: 0;
    background:
      radial-gradient(ellipse 40% 30% at 85% 72%, var(--fig-deep) 0%, transparent 100%),
      radial-gradient(ellipse 45% 35% at 70% 20%, var(--fig-mid) 0%, transparent 100%),
      radial-gradient(ellipse 40% 30% at 20% 15%, var(--fig-light) 0%, transparent 100%),
      linear-gradient(135deg, var(--fig-light) 0%, var(--label-white) 45%, var(--fig-mid) 100%);
  }
  .band {
    position: absolute;
    left: 0;
    top: 34px;
    width: 8px;
    height: 55px;
    display: flex;
    align-items: center;
    justify-content: center;
  }
  .band--orange { background: var(--band-orange); }
  .band--red { background: var(--band-red); }
  .band--crimson { background: var(--band-crimson); }
  .band__text {
    transform: rotate(-90deg);
    white-space: nowrap;
    font-family: "Oswald", Arial, sans-serif;
    font-weight: 500;
    font-size: 3.4px;
    letter-spacing: 0.3px;
    color: var(--panel-text);
  }
  .panel {
    position: absolute;
    left: 0;
    top: 34px;
    width: 65px;
    height: 55px;
    background: var(--panel-dark);
    color: var(--panel-text);
    text-align: center;
    padding-top: 8px;
  }
  .panel__name {
    font-weight: 600;
    font-size: 8px;
    line-height: 1;
  }
  .panel__motto {
    font-family: "Parisienne", cursive;
    font-size: 4.4px;
    line-height: 1;
    margin-top: 9px;
  }
  .panel__rule {
    width: 40px;
    height: 0.5px;
    background: var(--panel-text);
    opacity: 0.6;
    margin: 3px auto 2px;
  }
  .panel__bottler {
    font-family: "Oswald", Arial, sans-serif;
    font-size: 2.6px;
    line-height: 1.2;
    letter-spacing: 0.2px;
  }
  .panel__origin {
    font-size: 2.8px;
    line-height: 1.2;
    letter-spacing: 0.2px;
    margin-top: 1px;
  }
  .label__abv {
    position: absolute;
    left: 13px;
    bottom: 9px;
    font-family: "Oswald", Arial, sans-serif;
    font-weight: 500;
    font-size: 3.2px;
    letter-spacing: 0.3px;
    color: var(--ink);
  }
</style>
</head>
<body>
  <h1 class="brand-name">Volka Sereno</h1>

  <svg class="bottle bottle--classic" viewBox="0 0 127 497" aria-hidden="true">
    <path class="bottle__glass--pale" d="M40 100 L87 100 L88 140 C90 175 127 185 127 225 L127 480 Q127 497 110 497 L17 497 Q0 497 0 480 L0 225 C0 185 37 175 39 140 Z"/>
    <path class="bottle__cap--copper" d="M40 4 Q40 0 46 0 L81 0 Q87 0 87 4 L88 100 L39 100 Z"/>
  </svg>
  <svg class="bottle bottle--aged" viewBox="0 0 127 497" aria-hidden="true">
    <path class="bottle__glass--dark" d="M40 100 L87 100 L88 140 C90 175 127 185 127 225 L127 480 Q127 497 110 497 L17 497 Q0 497 0 480 L0 225 C0 185 37 175 39 140 Z"/>
    <path class="bottle__cap--wine" d="M40 4 Q40 0 46 0 L81 0 Q87 0 87 4 L88 100 L39 100 Z"/>
  </svg>
  <svg class="bottle bottle--light" viewBox="0 0 127 497" aria-hidden="true">
    <path class="bottle__glass--rose" d="M40 100 L87 100 L88 140 C90 175 127 185 127 225 L127 480 Q127 497 110 497 L17 497 Q0 497 0 480 L0 225 C0 185 37 175 39 140 Z"/>
    <path class="bottle__cap--rose" d="M40 4 Q40 0 46 0 L81 0 Q87 0 87 4 L88 100 L39 100 Z"/>
  </svg>

  <article class="label-wrap label-wrap--classic">
    <div class="band band--orange"><span class="band__text">LONDON DRY GIN</span></div>
    <div class="label">
      <div class="label__fig" role="img" aria-label="Engraved fig branch with leaves and fruit in pale gold"></div>
      <div class="panel">
        <p class="panel__name">Volka Sereno</p>
        <p class="panel__motto">Drink to Remember, Not to Forget!</p>
        <div class="panel__rule"></div>
        <p class="panel__bottler">BOTTLER NAME · LISBON 2019</p>
        <p class="panel__origin">PRODUCT FROM PORTUGAL</p>
      </div>
      <p class="label__abv">50% ABV</p>
    </div>
  </article>

  <article class="label-wrap label-wrap--aged">
    <div class="band band--red"><span class="band__text">LONDON DRY GIN</span></div>
    <div class="label">
      <div class="label__fig" role="img" aria-label="Engraved fig branch with leaves and fruit in pale gold"></div>
      <div class="panel">
        <p class="panel__name">Volka Sereno</p>
        <p class="panel__motto">Drink to Remember, Not to Forget!</p>
        <div class="panel__rule"></div>
        <p class="panel__bottler">BOTTLER NAME · LISBON 2019</p>
        <p class="panel__origin">PRODUCT FROM PORTUGAL</p>
      </div>
      <p class="label__abv">50% ABV</p>
    </div>
  </article>

  <article class="label-wrap label-wrap--light">
    <div class="band band--crimson"><span class="band__text">LONDON DRY GIN</span></div>
    <div class="label">
      <div class="label__fig" role="img" aria-label="Engraved fig branch with leaves and fruit in pale gold"></div>
      <div class="panel">
        <p class="panel__name">Volka Sereno</p>
        <p class="panel__motto">Drink to Remember, Not to Forget!</p>
        <div class="panel__rule"></div>
        <p class="panel__bottler">BOTTLER NAME · LISBON 2019</p>
        <p class="panel__origin">PRODUCT FROM PORTUGAL</p>
      </div>
      <p class="label__abv">50% ABV</p>
    </div>
  </article>
</body>
</html>
```